Website: mentorprogram for refugees; Uplift your tomorrow

We need a website for our project Kindlo, which mainly will serve as a information site for our stakeholders. (refugees/mentees, employers/mentors, municipality and sponsors)

We also need a logo/visual design program for the project. We are thinking something green/grey/blue - close to the logo used today. The design should communicate growth, understanding/integration, knowledge. The name Kindlo comes from refugees reframing/redesigning their future as part of the concept.

Kindlo is a two-dimensional consept/program to support refugees in redesigning their future and increasing their employability. The program offers a mentor to each refugee. Mentors will be trained in the mentor-role and will be instrumental in supporting the refugees in their quest to understand work culture in Norway. Understanding of intercultural communication and the value of diversity in the workplace is an important part of the program for both parties. Nature will provide a setting for the conversations between mentor and mentee

Logo Text

Kindlo

Number of Pages Required

1 page

Font styles to use
Sans Serif

Colors
9bcb3c
0355a3
f78f20

```html
<!DOCTYPE html>
<html lang="en">
<head>
<meta charset="utf-8">
<title>Kindlo Norway</title>
<link href="https://fonts.googleapis.com/css2?family=Questrial&family=Open+Sans:wght@400;600&display=swap" rel="stylesheet">
<style>
:root{
  --green:#3daa6a;
  --dark:#454545;
  --ink:#333333;
  --muted:#666666;
  --footer:#e3e3e3;
  --white:#ffffff;
  --accent:#e8573f;
}
*{box-sizing:border-box;margin:0;padding:0}
html,body{width:1200px;height:2542px;overflow:hidden}
body{position:relative;font-family:'Questrial',sans-serif;color:var(--ink);background:var(--white)}
.abs{position:absolute}
/* header */
.site-header{left:0;top:0;width:1200px;height:114px;background:var(--white)}
.brand{left:88px;top:28px;display:flex;align-items:center;gap:12px}
.brand-name{font-size:24px;letter-spacing:3px;color:var(--ink)}
.brand-mark{width:18px;height:18px;background:var(--green)}
.main-nav{right:88px;top:38px;display:flex;align-items:center;gap:42px;font-size:14px}
.main-nav span{color:var(--ink)}
.btn{display:inline-block;background:var(--green);color:var(--white);border-radius:22px;text-align:center}
.main-nav .btn{width:112px;height:38px;line-height:38px;font-size:14px;color:var(--white)}
/* hero */
.hero{left:0;top:114px;width:1200px;height:479px;background:linear-gradient(180deg,#6f88a8 0%,#5a6a72 45%,#4d5a44 100%)}
.hero-title{left:0;top:140px;width:1200px;text-align:center;color:var(--white);font-size:58px;line-height:68px;letter-spacing:1px}
.hero .btn{left:545px;top:288px;width:110px;height:38px;line-height:38px;font-size:14px}
.arrow{top:238px;width:28px;height:28px}
/* headings */
.section-title{left:0;width:1200px;text-align:center;font-size:32px;letter-spacing:1px;color:var(--ink)}
.section-title em{font-style:normal;color:var(--green)}
.title-rule{left:560px;width:80px;height:2px;background:var(--ink)}
.lead{left:0;width:1200px;text-align:center;font-size:14px;line-height:24px;color:var(--ink)}
/* about boxes */
.panel{height:124px;display:flex;align-items:center;color:var(--white);font-size:14px;line-height:22px;letter-spacing:.5px}
.panel-dark{left:88px;top:827px;width:515px;background:var(--dark);clip-path:polygon(0 0,100% 0,96% 100%,0 100%)}
.panel-green{left:597px;top:827px;width:516px;background:var(--green);clip-path:polygon(4% 0,100% 0,100% 100%,0 100%)}
.num{width:40px;height:40px;border-radius:50%;background:var(--white);color:var(--ink);font-size:14px;text-align:center;line-height:40px;flex:none}
.panel-dark .num{margin:0 22px 0 24px}
.panel-green .num{margin:0 22px 0 26px}
/* topics */
.topics{left:0;top:1041px;width:1200px;height:478px;background:radial-gradient(ellipse at 45% 40%,#3c4550 0%,#262b30 55%,#1b1e22 100%)}
.topics .section-title{color:var(--white)}
.topics .title-rule{background:var(--white)}
.topic-list{list-style:none;font-family:'Open Sans',sans-serif;font-size:12.5px;line-height:26.4px}
.topic-list.mentee{right:618px;top:146px;text-align:right;color:var(--green)}
.topic-list.mentor{left:617px;top:146px;color:var(--white)}
.tick{display:inline-block;width:11px;height:9px;margin:0 5px}
/* program */
.prog{height:246px;color:var(--white);text-align:center}
.prog-green{left:88px;top:1760px;width:515px;background:var(--green);clip-path:polygon(0 0,100% 0,98.5% 100%,0 100%)}
.prog-dark{left:597px;top:1760px;width:516px;background:var(--dark);clip-path:polygon(1.5% 0,100% 0,100% 100%,0 100%)}
.prog h3{font-weight:400;font-size:17px;letter-spacing:1px;margin-top:52px}
.prog p{font-family:'Open Sans',sans-serif;font-size:12px;line-height:21px;margin:14px auto 0;width:430px}
.prog .hl{color:var(--accent)}
.prog-num{top:1738px;width:44px;height:44px;border-radius:50%;background:var(--dark);color:var(--white);text-align:center;line-height:44px;font-size:14px}
.prog-num.two{background:var(--green)}
/* contact band */
.contact-band{left:0;top:2105px;width:1200px;height:91px;background:var(--green);color:var(--white);font-family:'Open Sans',sans-serif;font-size:18px}
.contact-item{top:34px;display:flex;align-items:center;gap:10px}
.divider{top:23px;width:1px;height:44px;background:rgba(255,255,255,.45)}
/* footer */
.site-footer{left:0;top:2196px;width:1200px;height:346px;background:var(--footer)}
.partner{top:80px}
.footer-heading{font-family:'Open Sans',sans-serif;font-size:21px;color:#555}
.field{left:528px;width:255px;height:48px;background:var(--white);border:1px solid #ccc;font-family:'Open Sans',sans-serif;font-size:12px;line-height:46px;padding-left:26px;color:#444}
.subscribe{left:528px;top:199px;width:255px;height:50px;line-height:50px;font-size:22px;border-radius:25px}
.sitemap{font-family:'Open Sans',sans-serif;font-size:11.5px;line-height:26px;color:#777;list-style:none}
.footer-rule{left:88px;top:278px;width:1025px;height:1px;background:#cfcfcf}
.copyright{left:88px;top:304px;font-family:'Open Sans',sans-serif;font-size:11.5px;color:#666}
.social{top:300px;display:flex;gap:26px}
.social span{width:16px;height:16px;border-radius:50%;background:#555;display:block}
</style>
</head>
<body>

<header class="site-header abs">
  <div class="brand abs"><span class="brand-name">Kindlo Norway</span><span class="brand-mark"></span></div>
  <nav class="main-nav abs">
    <span>Home</span><span>About</span><span>Services</span><span>Program</span><span>Support</span><span>Contact US</span>
    <span class="btn">Join Us</span>
  </nav>
</header>

<section class="hero abs" role="img" aria-label="Photo of a group of people walking away along a country road under a blue sky">
  <h1 class="hero-title abs">WELCOME TO<br>KINDLO NORWAY</h1>
  <span class="btn abs">Join Us</span>
  <svg class="arrow abs" style="left:30px" viewBox="0 0 28 28"><circle cx="14" cy="14" r="14" fill="#fff"/><path d="M16 8 L10 14 L16 20" stroke="#333" stroke-width="3" fill="none"/></svg>
  <svg class="arrow abs" style="left:1137px" viewBox="0 0 28 28"><circle cx="14" cy="14" r="14" fill="#fff"/><path d="M12 8 L18 14 L12 20" stroke="#333" stroke-width="3" fill="none"/></svg>
</section>

<h2 class="section-title abs" style="top:664px">ABOUT <em>KINDLO NORWAY</em></h2>
<div class="title-rule abs" style="top:714px"></div>
<p class="lead abs" style="top:748px">A two-dimensional consept to support refugees in redesigning their future and increasing their employability.<br>The program offers a mentor to each refugee. Mentors will be trained in the mentor-role</p>

<div class="panel panel-dark abs"><span class="num">01</span><span>A PROGRAM FOR REFUGEES PROVIDING SUPPORT FOR<br>REFRAMING WORK-LIFE IN A NEW CONTEXT</span></div>
<div class="panel panel-green abs"><span class="num">02</span><span>A MENTOR PROGRAM FOR LEADERS/ PROFESSIONALS<br>ACTING AS MENTORS FOR REFUGEES</span></div>

<section class="topics abs" role="img" aria-label="Dark photo of a man carrying a child on his shoulders among a crowd">
  <h2 class="section-title abs" style="top:60px">TOPICS <em>COVERED</em></h2>
  <div class="title-rule abs" style="top:110px;background:#fff"></div>
  <ul class="topic-list mentee abs">
    <li><svg class="tick" viewBox="0 0 11 9"><path d="M1 4.5 L4 7.5 L10 1" stroke="#3daa6a" stroke-width="2" fill="none"/></svg>Identity in a new context</li>
    <li><svg class="tick" viewBox="0 0 11 9"><path d="M1 4.5 L4 7.5 L10 1" stroke="#3daa6a" stroke-width="2" fill="none"/></svg>Self management</li>
    <li><svg class="tick" viewBox="0 0 11 9"><path d="M1 4.5 L4 7.5 L10 1" stroke="#3daa6a" stroke-width="2" fill="none"/></svg>How to build social capital</li>
    <li><svg class="tick" viewBox="0 0 11 9"><path d="M1 4.5 L4 7.5 L10 1" stroke="#3daa6a" stroke-width="2" fill="none"/></svg>Mindset – sitting in the 'driver's seat'</li>
    <li><svg class="tick" viewBox="0 0 11 9"><path d="M1 4.5 L4 7.5 L10 1" stroke="#3daa6a" stroke-width="2" fill="none"/></svg>Intercultural conflict resolution</li>
    <li><svg class="tick" viewBox="0 0 11 9"><path d="M1 4.5 L4 7.5 L10 1" stroke="#3daa6a" stroke-width="2" fill="none"/></svg>Resilience-training; dealing with rejection</li>
    <li><svg class="tick" viewBox="0 0 11 9"><path d="M1 4.5 L4 7.5 L10 1" stroke="#3daa6a" stroke-width="2" fill="none"/></svg>Trust in a Norwegian context</li>
    <li><svg class="tick" viewBox="0 0 11 9"><path d="M1 4.5 L4 7.5 L10 1" stroke="#3daa6a" stroke-width="2" fill="none"/></svg>Psychological contracts in Norwegian worklife</li>
    <li><svg class="tick" viewBox="0 0 11 9"><path d="M1 4.5 L4 7.5 L10 1" stroke="#3daa6a" stroke-width="2" fill="none"/></svg>How does masculinity &amp; femininity change in a new context</li>
  </ul>
  <ul class="topic-list mentor abs">
    <li><svg class="tick" viewBox="0 0 11 9"><path d="M1 4.5 L4 7.5 L10 1" stroke="#fff" stroke-width="2" fill="none"/></svg>Training for mentoring skills</li>
    <li><svg class="tick" viewBox="0 0 11 9"><path d="M1 4.5 L4 7.5 L10 1" stroke="#fff" stroke-width="2" fill="none"/></svg>Understanding organizational diversity</li>
    <li><svg class="tick" viewBox="0 0 11 9"><path d="M1 4.5 L4 7.5 L10 1" stroke="#fff" stroke-width="2" fill="none"/></svg>Building trust in a diverse culture</li>
    <li><svg class="tick" viewBox="0 0 11 9"><path d="M1 4.5 L4 7.5 L10 1" stroke="#fff" stroke-width="2" fill="none"/></svg>Understanding of basic  Norwegian work- and leadership styles</li>
    <li><svg class="tick" viewBox="0 0 11 9"><path d="M1 4.5 L4 7.5 L10 1" stroke="#fff" stroke-width="2" fill="none"/></svg>Understanding the basics of post-traumatic stress disorder</li>
    <li><svg class="tick" viewBox="0 0 11 9"><path d="M1 4.5 L4 7.5 L10 1" stroke="#fff" stroke-width="2" fill="none"/></svg>Intercultural conflict resolution</li>
    <li><svg class="tick" viewBox="0 0 11 9"><path d="M1 4.5 L4 7.5 L10 1" stroke="#fff" stroke-width="2" fill="none"/></svg>Bringing learning back to my organization</li>
  </ul>
</section>

<h2 class="section-title abs" style="top:1596px">PROGRAM <em>INNHOLD</em></h2>
<div class="title-rule abs" style="top:1646px"></div>
<p class="lead abs" style="top:1680px">Kindlo Norway består av to programmer som har noe overlapp</p>

<div class="prog prog-green abs">
  <h3>SELV-LEDELSES PROGRAM FOR FLYKTNINGER</h3>
  <p>Et 5-7 modulers program over 1 år (á 2-3 dager) med stor grad av individuell tilpasning. Det overordnede programmet tilpasses den enkelte kommune basert på deres eksisterende integreringsarbeid</p>
</div>
<div class="prog prog-dark abs">
  <h3>KINDLO MENTORPROGRAM</h3>
  <p>Et 3-4 modulers program der ledere/fagpersoner fra lokale organisasjoner (privat eller offentlig sektor) etter avtale med sin arbeidsgiver stiller som  mentor for en flyktning. Disse mentorene vil få et grundig mentor-treningsprogram som også kan anvendes i den organisasjonen <span class="hl">de</span> jobber til daglig Det forventes at mentorene bruker <span class="hl">4-6</span> arbeidsdager <span class="hl">da ¾ år</span> og noe av sin fritid som mentor for en flyktning</p>
</div>
<div class="prog-num abs" style="left:102px">01</div>
<div class="prog-num two abs" style="left:612px">02</div>

<section class="contact-band abs">
  <div class="contact-item abs" style="left:208px">
    <svg width="12" height="16" viewBox="0 0 12 16"><path d="M6 0a6 6 0 0 1 6 6c0 4-6 10-6 10S0 10 0 6a6 6 0 0 1 6-6z" fill="#fff"/><circle cx="6" cy="6" r="2.2" fill="#3daa6a"/></svg>
    <span>Lindeveien 12, SOLBERG, N/A, 1520.</span>
  </div>
  <div class="divider abs" style="left:572px"></div>
  <div class="contact-item abs" style="left:616px">
    <svg width="15" height="15" viewBox="0 0 15 15"><path d="M3 0l3 3.5-1.6 2a9 9 0 0 0 5 5l2-1.6L15 12l-2 3C6 15 0 9 0 2z" fill="#fff"/></svg>
    <span>455 18 902</span>
  </div>
  <div class="divider abs" style="left:775px"></div>
  <div class="contact-item abs" style="left:824px">
    <svg width="17" height="13" viewBox="0 0 17 13"><rect width="17" height="13" rx="1.5" fill="#fff"/><path d="M1 1.5l7.5 6 7.5-6" stroke="#3daa6a" stroke-width="1.5" fill="none"/></svg>
    <span>info@kindlo.no</span>
  </div>
</section>

<footer class="site-footer abs">
  <svg class="partner abs" style="left:88px" width="116" height="120" viewBox="0 0 116 120" role="img" aria-label="Partner badge"><circle cx="58" cy="60" r="56" fill="none" stroke="#2e3f8f" stroke-width="3"/></svg>
  <svg class="partner abs" style="left:248px" width="116" height="140" viewBox="0 0 116 140" role="img" aria-label="Partner badge"><rect x="10" y="10" width="96" height="96" fill="#6bb04a"/></svg>

  <div class="footer-heading abs" style="left:540px;top:36px">Join Our Newsletter</div>
  <div class="field abs" style="top:81px">Name</div>
  <div class="field abs" style="top:138px">Email</div>
  <div class="btn subscribe abs">subscribe</div>

  <div class="footer-heading abs" style="left:910px;top:36px">Sitemap</div>
  <ul class="sitemap abs" style="left:910px;top:82px"><li>&gt; Home</li><li>&gt; Program</li><li>&gt; Services</li><li>&gt; Support</li></ul>
  <ul class="sitemap abs" style="left:1016px;top:82px"><li>&gt; About</li><li>&gt; Privacy Policy</li><li>&gt; Contact</li></ul>

  <div class="footer-rule abs"></div>
  <p class="copyright abs">Copyright © 2017 Kindlo Norway. All Rights Reserved.</p>
  <div class="social abs" style="left:952px"><span></span><span></span><span></span><span></span></div>
</footer>

</body>
</html>
```